Korvex Systems*

Stationary design including business cards, letter heads, envelops and email signatures using our new logo

Target Market(s)

Innovative Technologies

Industry/Entity Type

Defense Contracting

Font styles to use
Sans Serif

```html
<!DOCTYPE html>
<html lang="en">
<head>
<meta charset="utf-8">
<title>Korvex Systems Stationery</title>
<link href="https://fonts.googleapis.com/css2?family=Montserrat:wght@300;400;500&family=Roboto:wght@400&display=swap" rel="stylesheet">
<style>
  :root{
    --backdrop:#d9d9d9;
    --paper:#ffffff;
    --ink:#1c1c1c;
    --ink-soft:#5a5a5a;
    --ink-faint:#8c8c8c;
    --rule:#bdbdbd;
    --band-dark:#0d0d0d;
    --band-grey:#6b6b6b;
  }
  *{margin:0;padding:0;box-sizing:border-box;}
  html,body{width:1200px;height:1200px;overflow:hidden;background:var(--backdrop);}
  body{position:relative;font-family:"Montserrat",sans-serif;color:var(--ink);}
  .sheet{position:absolute;background:var(--paper);box-shadow:0 2px 6px rgba(0,0,0,.25);overflow:hidden;}
  .abs{position:absolute;}

  .letterhead{left:61px;top:254px;width:491px;height:692px;}
  .brand{display:flex;align-items:center;gap:5px;font-family:"Montserrat",sans-serif;font-weight:500;font-size:10px;letter-spacing:.3px;color:var(--ink);white-space:nowrap;}
  .brand-square{width:7px;height:7px;border:1px solid var(--ink);}
  .letterhead .brand{left:44px;top:60px;}
  .header-rule{left:30px;top:83px;width:431px;height:1px;background:var(--rule);}
  .contact{left:370px;top:22px;font-family:"Roboto",sans-serif;font-size:7.6px;line-height:9px;color:var(--ink);}
  .contact p{margin:0;}
  .contact .row{display:flex;align-items:center;gap:5px;margin-top:2.6px;}
  .contact svg{width:6px;height:6px;flex:none;}
  .contact .address{margin-bottom:2px;}
  .to{left:49px;top:154px;font-size:9px;letter-spacing:1.5px;color:var(--ink-soft);}
  .date{right:51px;top:154px;font-size:7px;color:var(--ink-soft);}
  .recipient{left:49px;top:168px;font-size:8.2px;color:var(--ink);}
  .recipient-lines{left:49px;top:182px;font-size:6.4px;line-height:10.8px;color:var(--ink-faint);font-weight:300;}
  .body-copy{left:49px;top:250px;width:392px;font-size:6.6px;line-height:8.7px;color:var(--ink-faint);font-weight:300;text-align:justify;}
  .body-copy p{margin-bottom:8.6px;}
  .signature{left:48px;top:488px;width:86px;height:16px;background:linear-gradient(90deg,#e6e6e6,#f2f2f2);border-radius:2px;}
  .signer{left:49px;top:514px;font-size:7.6px;color:var(--ink);}
  .signer-role{left:49px;top:525px;font-size:6px;color:var(--ink-faint);}
  .band{left:0;bottom:0;width:100%;height:12px;}

  .envelope-back{left:576px;top:433px;width:563px;height:244px;box-shadow:0 1px 4px rgba(0,0,0,.2);}
  .flap{left:0;top:0;width:563px;height:80px;}
  .envelope-back .brand{left:50%;top:44px;transform:translateX(-50%);}
  .web{left:0;top:226px;width:100%;text-align:center;font-size:7.6px;letter-spacing:2px;color:var(--ink);}

  .envelope-front{left:576px;top:702px;width:563px;height:244px;}
  .envelope-front .brand{left:20px;top:62px;}
  .return-address{left:20px;top:81px;width:88px;text-align:center;font-family:"Roboto",sans-serif;font-size:7.6px;line-height:9.6px;color:var(--ink);}
</style>
</head>
<body>

<section class="sheet letterhead">
  <div class="abs brand"><span class="brand-square"></span>Korvex Systems</div>
  <div class="abs contact">
    <p class="address">2240-B Ridgeline Ave,<br>Arlen, W41</p>
    <div class="row"><svg viewBox="0 0 10 10"><path d="M2 1l2 .3.6 2.2-1.2.9a6 6 0 0 0 2.2 2.2l.9-1.2 2.2.6.3 2c-4 .8-8-3.2-7-7z" fill="#1c1c1c"/></svg>555-014-2100</div>
    <div class="row"><svg viewBox="0 0 10 10"><rect x="1" y="2" width="8" height="6" fill="none" stroke="#1c1c1c" stroke-width="1"/><path d="M1 2l4 3.5L9 2" fill="none" stroke="#1c1c1c" stroke-width="1"/></svg>office@korvexsystems.com</div>
    <div class="row"><svg viewBox="0 0 10 10"><circle cx="5" cy="5" r="4" fill="none" stroke="#1c1c1c" stroke-width="1"/><ellipse cx="5" cy="5" rx="1.8" ry="4" fill="none" stroke="#1c1c1c" stroke-width=".8"/><path d="M1 5h8" stroke="#1c1c1c" stroke-width=".8"/></svg>www.korvexsystems.com</div>
  </div>
  <div class="abs header-rule"></div>

  <div class="abs to">TO</div>
  <div class="abs date">Friday, 01/01/2018</div>
  <div class="abs recipient">Dana Whitlow</div>
  <div class="abs recipient-lines">Human Resources<br>Northfield Avionics Inc.<br>2240-B Ridgeline Ave, Arlen<br>W41 USA</div>

  <div class="abs body-copy">
    <p>Lorem ipsum dolor sit amet, consectetuer adipiscing elit, sed diam nonummy nibh euismod tincidunt ut laoreet dolore magna aliquam erat volutpat. Ut wisi enim ad minim veniam, quis nostrud exerci tation ullamcorper suscipit lobortis nisl ut aliquip ex ea commodo consequat. Duis autem vel eum iriure dolor in hendrerit in vulputate velit esse molestie consequat, vel illum dolore eu feugiat nulla facilisis at vero eros et accumsan et iusto odio dignissim qui blandit praesent luptatum zzril delenit augue duis dolore te feugait nulla facilisi.</p>
    <p>Nam liber tempor cum soluta nobis eleifend option congue nihil imperdiet doming id quod mazim placerat facer possim assum. Typi non habent claritatem insitam;</p>
    <p>Est usus legentis in iis qui facit eorum claritatem.</p>
    <p>Investigationes demonstraverunt lectores legere me lius quod ii legunt saepius. Claritas est etiam processus dynamicus, qui sequitur mutationem consuetudium lectorum. Mirum est notare quam littera gothica, quam nunc putamus parum claram, anteposuerit litterarum formas humanitatis per seacula quarta decima et quinta decima. Eodem modo typi, qui nunc nobis videntur parum clari, fiant sollemnes in futurum.</p>
    <p>consectetuer adipiscing elit, sed diam nonummy nibh euismod tincidunt ut laoreet dolore magna aliquam erat volutpat. Ut wisi enim ad minim veniam, quis nostrud exerci tation ullamcorper suscipit lobortis nisl ut aliquip ex ea commodo consequat. Duis autem vel eum iriure dolor in hendrerit in vulputate velit esse molestie consequat, vel illum dolore eu feugiat nulla facilisis at vero eros et accumsan et iusto odio dignissim qui blandit praesent luptatum zzril delenit augue duis dolore te feugait nulla facilisi.</p>
    <p>Nam liber tempor cum soluta nobis eleifend option congue nihil imperdiet.</p>
  </div>

  <div class="abs signature" role="img" aria-label="Handwritten signature of Evan Calder"></div>
  <div class="abs signer">Evan Calder</div>
  <div class="abs signer-role">Managing Director</div>

  <svg class="abs band" viewBox="0 0 491 12" preserveAspectRatio="none">
    <polygon points="0,0 418,0 412,12 0,12" fill="var(--band-dark)"/>
    <polygon points="422,0 491,0 491,12 416,12" fill="var(--band-grey)"/>
  </svg>
</section>

<section class="sheet envelope-back">
  <svg class="abs flap" viewBox="0 0 563 80">
    <defs>
      <filter id="flap-shadow" x="-5%" y="-20%" width="110%" height="160%">
        <feDropShadow dx="0" dy="3" stdDeviation="3" flood-color="#000" flood-opacity=".28"/>
      </filter>
    </defs>
    <path d="M0 0 H563 L556 20 Q548 58 520 66 H43 Q15 58 7 20 Z" fill="var(--paper)" filter="url(#flap-shadow)"/>
  </svg>
  <div class="abs brand"><span class="brand-square"></span>Korvex Systems</div>
  <div class="abs web">www.korvexsystems.com</div>
</section>

<section class="sheet envelope-front">
  <div class="abs brand"><span class="brand-square"></span>Korvex Systems</div>
  <div class="abs return-address">2240-B Ridgeline Ave,<br>Arlen, W41</div>
  <svg class="abs band" viewBox="0 0 563 12" preserveAspectRatio="none">
    <polygon points="0,0 483,0 477,12 0,12" fill="var(--band-dark)"/>
    <polygon points="487,0 563,0 563,12 481,12" fill="var(--band-grey)"/>
  </svg>
</section>

</body>
</html>
```